Harborstone Lending Business Card Design

We are looking for a nice looking business card design. I'd prefer something other than white for the background but white is ok if necessary. I'm uploading two versions of my picture, one is square and one is rounded. Also a couple of versions of the logo for white backgrounds as well as one for darker backgrounds.

Target Market(s)

Realtors and prospective clients

Industry/Entity Type

Mortgage

Contact Information for Business Card

Double sided business card. Not sure what is needed here.

Colors

Designer to choose colors to be used in the design.

Requirements
Must have
• Name: Marcus Pellham
• Title: Senior Mortgage Advisor
• Email: marcuspellham@harborstonelending.example
• website: www.marcuspellhamhomeloangroup.example
• Address: 4670 W 2850 N, STE 215 Salt Lake City, UT 84192
• Phone: 801-555-0187
• nmls# 948217
• Logo is on our webstie. www.harborstonelending.example
• Picture
Nice to have
• Colors could be similar to our website www.harborstonelending.example
• A list of what we do (VA Loans, FHA Loans, Conventional Loans, USDA Loans)

```html
<!DOCTYPE html>
<html lang="en">
<head>
<meta charset="utf-8">
<title>Harborstone Lending Business Card</title>
<link rel="stylesheet" href="https://fonts.googleapis.com/css2?family=Roboto:wght@400;500;700&family=Roboto+Condensed:wght@500;700&display=swap">
<style>
  :root {
    --backdrop: #d9b894;
    --card-white: #f3f3f3;
    --card-dark: #222222;
    --ink: #1e1e1e;
    --ink-soft: #474747;
    --emblem-tone: #dcdcdc;
    --on-dark: #ffffff;
  }
  * { margin: 0; padding: 0; box-sizing: border-box; }
  html, body { width: 1200px; height: 960px; overflow: hidden; }
  body {
    position: relative;
    background: var(--backdrop);
    font-family: "Roboto", Arial, sans-serif;
  }
  .card {
    position: absolute;
    left: 320px;
    width: 600px;
    border-radius: 14px;
    overflow: hidden;
    background: var(--card-white);
  }

  /* Front side */
  .card--front { top: 95px; height: 355px; }
  .front__emblem-area {
    position: absolute;
    left: 320px; top: 40px;
    width: 280px; height: 315px;
    background: radial-gradient(ellipse at 55% 55%, var(--emblem-tone) 0%, rgba(220,220,220,0.35) 55%, rgba(243,243,243,0) 80%);
  }
  .front__brand {
    position: absolute;
    left: 35px; top: 200px;
    font-size: 24px;
    font-weight: 700;
    letter-spacing: 2px;
    color: var(--ink);
    text-transform: uppercase;
  }
  .services {
    position: absolute;
    left: 35px; top: 248px;
    list-style: none;
  }
  .services li {
    display: flex;
    align-items: center;
    height: 20px;
    font-size: 14.5px;
    color: var(--ink-soft);
  }
  .services svg { width: 9px; height: 9px; margin-right: 9px; fill: var(--ink); }

  /* Back side */
  .card--back { top: 493px; height: 342px; }
  .back__panel {
    position: absolute;
    left: 0; top: 0;
    width: 330px; height: 100%;
    background: var(--card-dark);
    color: var(--on-dark);
    overflow: hidden;
  }
  .back__divider {
    position: absolute;
    left: 334px; top: 0;
    width: 4px; height: 100%;
    background: var(--card-dark);
  }
  .person__name {
    position: absolute;
    left: 28px; top: 30px;
    font-family: "Roboto Condensed", "Arial Narrow", sans-serif;
    font-weight: 700;
    font-size: 22px;
    text-transform: uppercase;
  }
  .person__title {
    position: absolute;
    left: 28px; top: 56px;
    font-size: 15px;
    font-weight: 500;
    text-transform: uppercase;
  }
  .office {
    position: absolute;
    left: 28px; top: 192px;
    font-size: 14.5px;
    line-height: 18px;
  }
  .contacts {
    position: absolute;
    left: 28px; top: 256px;
    list-style: none;
    font-size: 13px;
    letter-spacing: -0.1px;
  }
  .contacts li { display: flex; align-items: center; height: 19.5px; white-space: nowrap; }
  .contacts svg { width: 12px; height: 12px; margin-right: 9px; fill: var(--on-dark); flex: none; }
  .back__brand {
    position: absolute;
    left: 346px; top: 155px;
    width: 254px;
    display: flex;
    align-items: center;
    justify-content: center;
    gap: 8px;
    font-size: 15px;
    font-weight: 700;
    letter-spacing: 1px;
    color: var(--ink);
    text-transform: uppercase;
    white-space: nowrap;
  }
  .back__brand-dot {
    width: 18px; height: 18px;
    border-radius: 50%;
    background: var(--ink);
    flex: none;
  }
</style>
</head>
<body>
  <section class="card card--front">
    <div class="front__emblem-area" role="img" aria-label="Faint large brand emblem decoration"></div>
    <div class="front__brand">Harborstone Lending</div>
    <ul class="services">
      <li><svg viewBox="0 0 10 10"><polygon points="5,0 6.2,3.6 10,3.6 6.9,5.8 8.1,9.5 5,7.2 1.9,9.5 3.1,5.8 0,3.6 3.8,3.6"/></svg>VA Loans</li>
      <li><svg viewBox="0 0 10 10"><polygon points="5,0 6.2,3.6 10,3.6 6.9,5.8 8.1,9.5 5,7.2 1.9,9.5 3.1,5.8 0,3.6 3.8,3.6"/></svg>FHA Loans</li>
      <li><svg viewBox="0 0 10 10"><polygon points="5,0 6.2,3.6 10,3.6 6.9,5.8 8.1,9.5 5,7.2 1.9,9.5 3.1,5.8 0,3.6 3.8,3.6"/></svg>Conventional Loans</li>
      <li><svg viewBox="0 0 10 10"><polygon points="5,0 6.2,3.6 10,3.6 6.9,5.8 8.1,9.5 5,7.2 1.9,9.5 3.1,5.8 0,3.6 3.8,3.6"/></svg>USDA Loans</li>
    </ul>
  </section>

  <section class="card card--back">
    <div class="back__panel">
      <h1 class="person__name">Marcus Pellham</h1>
      <p class="person__title">Senior Mortgage Advisor</p>
      <p class="office">4670 W 2850 N, STE 215<br>Salt Lake City, UT 84192<br>nmls# 948217</p>
      <ul class="contacts">
        <li><svg viewBox="0 0 24 24"><path d="M6.6 10.8a15.1 15.1 0 0 0 6.6 6.6l2.2-2.2c.3-.3.7-.4 1-.2 1.1.4 2.3.6 3.6.6.6 0 1 .4 1 1V20c0 .6-.4 1-1 1A17 17 0 0 1 3 4c0-.6.4-1 1-1h3.5c.6 0 1 .4 1 1 0 1.3.2 2.5.6 3.6.1.3 0 .7-.2 1z"/></svg>801-555-0187</li>
        <li><svg viewBox="0 0 24 24"><path d="M2 6.5l10 7 10-7V19H2z"/><path d="M2 5h20l-10 7z"/></svg>marcuspellham@harborstonelending.example</li>
        <li><svg viewBox="0 0 24 24"><path d="M12 2a10 10 0 1 0 0 20 10 10 0 0 0 0-20zm-1 17.9A8 8 0 0 1 4.2 10.6L9 15.4v1a2 2 0 0 0 2 2zm6.9-2.5a2 2 0 0 0-1.9-1.4h-1v-3a1 1 0 0 0-1-1H8v-2h2a1 1 0 0 0 1-1V7h2a2 2 0 0 0 2-2v-.4a8 8 0 0 1 2.9 12.8z"/></svg>marcuspellhamhomeloangroup.example</li>
      </ul>
    </div>
    <div class="back__divider"></div>
    <div class="back__brand"><span class="back__brand-dot"></span>Harborstone Lending</div>
  </section>
</body>
</html>
```